Marisol Lodge website redesign

After 8 years of our current site, we're ready to upgrade our site design. We'd like to generally make it more modern and clean and build it on a CMS like joomla for easier future maintenance.

Our hotel is a family-owned bed and breakfast that competes against much larger hotel chains in Aspen with fancier rooms and larger pricetags. Our hotel is priced moderately and features tasteful, uniquely-design rooms.

We are looking for a website that will showcase the uniqueness of our rooms, the history of the Lodge, and the friendliness of our staff.

Here are some other hotel sites we like:

http://www.thecopperwren.example/

http://www.pinecrestridgehouse.example/

http://www.hotelbrivaro.example/

*********

Scope of Work - I'm looking for a design AND build. The website should be built out in Joomla as part of the final deliverable.

Current website: http://www.marisollodge.example/

Explanation of what design + build means:

I am looking for not only the design of the site, but also for the homepage and one subpage to be built out as well. I do NOT need the entire site built - only for those two pages to be built and I will retrofit the remainder of the pages.

Target Market(s)

travellers evaluating hotels in Aspen, Colorado.

Industry/Entity Type

Hotel

Requirements
Must have
• Must, must, must be based on a joomla template. "Rotating" large main image as central position on homepage is a must (see example websites mentioned above).

Nice to have
• We have an existing online reservation system. It would be nice to evaluate placing a "widget" on the homepage that integrates to the online reservation page. Similar to that feature that the Copper Wren website has at the foot of the main image on their homepage.

```html
<!DOCTYPE html>
<html lang="en">
<head>
<meta charset="utf-8">
<title>Marisol Lodge</title>
<link rel="stylesheet" href="https://fonts.googleapis.com/css2?family=Noto+Sans:wght@400;700&family=Exo+2:ital,wght@1,700&display=swap">
<style>
  :root {
    --rust: #8f2a14;
    --rust-dark: #7a220f;
    --rust-btn: #8a3a26;
    --nav-active: #a82b12;
    --nav-text: #f1d7cc;
    --charcoal: #2a2a2a;
    --panel-welcome: #4a4645;
    --panel-gallery: #353231;
    --body-text: #f2efed;
    --accent: #ff4a12;
    --btn-text: #d9c9c2;
    --thumb-border: #f4f4f4;
  }
  * { box-sizing: border-box; margin: 0; padding: 0; }
  html, body { width: 1200px; height: 994px; overflow: hidden; }
  body {
    position: relative;
    background: var(--charcoal);
    font-family: "Noto Sans", Verdana, sans-serif;
    color: var(--body-text);
  }
  .site-nav {
    position: absolute; left: 0; top: 0; width: 1200px; height: 50px;
    background: linear-gradient(#a0341a, var(--rust));
    z-index: 3;
  }
  .nav-link {
    position: absolute; top: 0; height: 50px; line-height: 52px;
    transform: translateX(-50%);
    font-size: 14px; color: var(--nav-text); text-decoration: none; white-space: nowrap;
  }
  .nav-link.is-active {
    left: 52px; width: 134px; transform: none; text-align: center;
    top: 9px; height: 36px; line-height: 36px; background: var(--nav-active);
  }
  .hero {
    position: absolute; left: 0; top: 50px; width: 1200px; height: 542px;
    background:
      linear-gradient(90deg, rgba(255,236,190,.55) 0%, rgba(120,80,40,.15) 45%, rgba(215,205,240,.55) 80%, rgba(250,235,200,.4) 100%),
      linear-gradient(180deg, #c9a86a 0%, #8a6336 55%, #5a3d22 100%);
    border-bottom: 8px solid #a8361a;
  }
  .brand-tab {
    position: absolute; left: 0; top: 67px; width: 274px; height: 67px;
    background: var(--rust-btn); border-radius: 0 10px 10px 0;
    display: flex; align-items: center; padding-left: 22px; z-index: 2;
  }
  .brand-name { font-size: 27px; font-weight: 400; color: #fff; }
  .availability-btn {
    position: absolute; left: 285px; top: 500px; width: 606px; height: 66px;
    background: var(--rust-btn); border-radius: 10px; z-index: 2;
    display: flex; align-items: center; justify-content: center;
    font-size: 22px; font-weight: 700; color: var(--btn-text); text-decoration: none;
  }
  .welcome {
    position: absolute; left: 52px; top: 592px; width: 1099px; height: 145px;
    background: var(--panel-welcome); padding: 15px 52px 0;
  }
  .section-title {
    font-family: "Exo 2", Verdana, sans-serif; font-style: italic; font-weight: 700;
    color: #fff;
  }
  .welcome .section-title { font-size: 24px; line-height: 30px; margin-bottom: 8px; }
  .welcome .section-title .initial { color: var(--accent); }
  .welcome p { font-size: 11.5px; line-height: 14px; margin-bottom: 12px; }
  .gallery {
    position: absolute; left: 52px; top: 737px; width: 1099px; height: 168px;
    background: var(--panel-gallery);
  }
  .gallery .section-title { position: absolute; left: 56px; top: 22px; font-size: 17px; }
  .thumb {
    position: absolute; top: 57px; width: 111px; height: 92px;
    border: 2px solid var(--thumb-border);
    background: linear-gradient(135deg, #c8b89a 0%, #8a7050 45%, #b07080 70%, #e4dccf 100%);
  }
  .site-footer {
    position: absolute; left: 0; top: 920px; width: 1200px; height: 51px;
    background: var(--rust);
  }
  .follow {
    position: absolute; left: 52px; top: 10px; height: 34px;
    display: flex; align-items: center; gap: 8px;
    font-size: 14px; font-weight: 700; color: #fff;
  }
  .follow .mark { width: 22px; height: 22px; background: #fff; }
  .copyright {
    position: absolute; right: 48px; top: 0; line-height: 51px;
    font-size: 13px; color: var(--nav-text);
  }
  .copyright .sep { margin: 0 12px; }
</style>
</head>
<body>
  <nav class="site-nav">
    <a class="nav-link is-active" href="#">About the Lodge</a>
    <a class="nav-link" style="left:258px" href="#">Rooms</a>
    <a class="nav-link" style="left:389px" href="#">Reservation</a>
    <a class="nav-link" style="left:523px" href="#">Amenities</a>
    <a class="nav-link" style="left:679px" href="#">Aspen Information</a>
    <a class="nav-link" style="left:864px" href="#">Manager's Journal</a>
    <a class="nav-link" style="left:1008px" href="#">Webcams</a>
    <a class="nav-link" style="left:1117px" href="#">Contact Us</a>
  </nav>

  <div class="hero" role="img" aria-label="Rotating photo of a guest room with a four-poster bed, gold curtains, green armchairs and roses"></div>
  <div class="brand-tab"><span class="brand-name">Marisol Lodge</span></div>
  <a class="availability-btn" href="#">Check Availability &amp; Rates</a>

  <section class="welcome">
    <h1 class="section-title"><span class="initial">W</span>elcome ...</h1>
    <p>Located in the heart of downtown Aspen, the newly renovated Marisol Lodge possesses all the charms of a vintage European Ski Lodge, while offering all of the modern conveniences one would expect with a stay in Aspen.</p>
    <p>A stay at our lodge includes free continental breakfast in our dining room, daily maid service, free wireless internet access, and a fully-equipped conference facility. Guests are also invited to relax in one of our two outdoor hot tubs or in our lounge, where a 42-inch plasma TV and fireplace make for a pleasant area to unwind.</p>
  </section>

  <section class="gallery">
    <h2 class="section-title">Our Gallery</h2>
    <div class="thumb" style="left:56px" role="img" aria-label="Guest room with canopy bed"></div>
    <div class="thumb" style="left:193px" role="img" aria-label="Guest room with canopy bed"></div>
    <div class="thumb" style="left:338px" role="img" aria-label="Guest room with canopy bed"></div>
    <div class="thumb" style="left:481px" role="img" aria-label="Guest room with canopy bed"></div>
    <div class="thumb" style="left:623px" role="img" aria-label="Guest room with canopy bed"></div>
    <div class="thumb" style="left:766px" role="img" aria-label="Guest room with canopy bed"></div>
    <div class="thumb" style="left:909px" role="img" aria-label="Guest room with canopy bed"></div>
  </section>

  <footer class="site-footer">
    <div class="follow"><span class="mark"></span>Follow us online</div>
    <div class="copyright">© 2005 Marisol Lodge<span class="sep">|</span>info@marisollodge.example</div>
  </footer>
</body>
</html>
```